Business Card Design Project

Need professional business card and Employee Badge design for a young dynamic and emp friendly IT Services company.

Target Market(s)

IT, Corporate

Industry/Entity Type

Business

Requirements
Must have
• Modern, Sleek, Prfessional, IT services
Should not have
• Too much diffrent colors

```html
<!DOCTYPE html>
<html lang="en">
<head>
<meta charset="utf-8">
<title>Veltrix Technologies – Business Card</title>
<link href="https://fonts.googleapis.com/css2?family=Open+Sans:wght@400;600;700&display=swap" rel="stylesheet">
<style>
  :root {
    --page: #e9e7e4;
    --white: #ffffff;
    --red: #d81b4c;
    --rust: #a8362a;
    --grey: #8d8d8f;
    --ink-light: #ffffff;
    --shadow: rgba(0,0,0,0.22);
  }
  * { margin: 0; padding: 0; box-sizing: border-box; }
  html, body { width: 1200px; height: 1024px; overflow: hidden; }
  body {
    background: var(--page);
    font-family: "Open Sans", Arial, sans-serif;
    position: relative;
  }
  .card {
    position: absolute;
    left: 250px;
    width: 700px;
    height: 400px;
    overflow: hidden;
    box-shadow: 0 10px 26px var(--shadow);
  }
  .card--front { top: 82px; background: var(--white); }
  .card--back { top: 542px; }
  .card__art { position: absolute; inset: 0; width: 100%; height: 100%; }

  .brand {
    position: absolute;
    font-weight: 700;
    letter-spacing: 0.5px;
    white-space: nowrap;
  }
  .card--front .brand { left: 48px; top: 70px; font-size: 40px; color: var(--red); }
  .card--back .brand { left: 150px; top: 150px; font-size: 44px; color: var(--ink-light); }

  .contact {
    position: absolute;
    left: 48px;
    top: 190px;
    color: var(--ink-light);
  }
  .contact__name { font-weight: 700; font-size: 20px; letter-spacing: 0.5px; text-transform: uppercase; }
  .contact__role { font-weight: 600; font-size: 15px; letter-spacing: 0.5px; text-transform: uppercase; margin-bottom: 10px; }
  .contact__list { list-style: none; }
  .contact__item {
    display: flex; align-items: center; gap: 10px;
    font-size: 15px; line-height: 24px;
  }
  .contact__icon { width: 14px; height: 14px; flex: none; }

  .website {
    position: absolute;
    left: 34px; top: 26px;
    font-size: 14px;
    color: var(--ink-light);
    letter-spacing: 0.3px;
  }
</style>
</head>
<body>

<section class="card card--front" aria-label="Business card front">
  <svg class="card__art" viewBox="0 0 700 400" preserveAspectRatio="none" aria-hidden="true">
    <defs>
      <linearGradient id="frontBand" x1="0" y1="1" x2="1" y2="0">
        <stop offset="0" stop-color="#a8362a"/>
        <stop offset="0.5" stop-color="#d81b4c"/>
        <stop offset="1" stop-color="#b1332b"/>
      </linearGradient>
    </defs>
    <rect x="0" y="170" width="700" height="230" fill="url(#frontBand)"/>
    <polygon points="530,0 566,0 616,170 580,170" fill="#a8362a"/>
    <polygon points="566,0 604,0 654,170 616,170" fill="#ffffff"/>
    <polygon points="604,0 700,0 700,170 654,170" fill="#8d8d8f"/>
  </svg>

  <div class="brand">Veltrix Technologies</div>

  <div class="contact">
    <p class="contact__name">Marcus Hale</p>
    <p class="contact__role">Job Title</p>
    <ul class="contact__list">
      <li class="contact__item">
        <svg class="contact__icon" viewBox="0 0 14 14" aria-hidden="true"><path d="M3 1l2 3-1.3 1.4a8 8 0 004.9 4.9L10 9l3 2-1 2.5C6 13 1 8 .5 2z" fill="#fff"/></svg>
        +1 555 0142 281
      </li>
      <li class="contact__item">
        <svg class="contact__icon" viewBox="0 0 14 14" aria-hidden="true"><rect x="3.5" y="0.5" width="7" height="13" rx="1.3" fill="none" stroke="#fff" stroke-width="1.3"/><circle cx="7" cy="11" r="0.9" fill="#fff"/></svg>
        +1 555 0142 282
      </li>
      <li class="contact__item">
        <svg class="contact__icon" viewBox="0 0 14 14" aria-hidden="true"><rect x="1" y="5" width="12" height="7" rx="1" fill="#fff"/><rect x="3.5" y="1" width="7" height="4" fill="none" stroke="#fff" stroke-width="1.2"/></svg>
        +1 555 0187 930
      </li>
      <li class="contact__item">
        <svg class="contact__icon" viewBox="0 0 14 14" aria-hidden="true"><rect x="0.7" y="2.5" width="12.6" height="9" fill="none" stroke="#fff" stroke-width="1.3"/><path d="M1 3l6 5 6-5" fill="none" stroke="#fff" stroke-width="1.3"/></svg>
        marcus@veltrixtech.com
      </li>
      <li class="contact__item">
        <svg class="contact__icon" viewBox="0 0 14 14" aria-hidden="true"><circle cx="7" cy="7" r="6" fill="none" stroke="#fff" stroke-width="1.2"/><ellipse cx="7" cy="7" rx="2.6" ry="6" fill="none" stroke="#fff" stroke-width="1"/><path d="M1 7h12" stroke="#fff" stroke-width="1"/></svg>
        www.veltrixtech.com
      </li>
    </ul>
  </div>
</section>

<section class="card card--back" aria-label="Business card back">
  <svg class="card__art" viewBox="0 0 700 400" preserveAspectRatio="none" aria-hidden="true">
    <defs>
      <linearGradient id="backBand" x1="0" y1="0" x2="1" y2="1">
        <stop offset="0" stop-color="#b1332b"/>
        <stop offset="0.55" stop-color="#d81b4c"/>
        <stop offset="1" stop-color="#a8362a"/>
      </linearGradient>
    </defs>
    <rect x="0" y="0" width="700" height="400" fill="url(#backBand)"/>
    <polygon points="0,318 700,292 700,400 0,400" fill="#ffffff"/>
    <polygon points="110,302 700,268 700,292 380,304" fill="#a8362a"/>
    <polygon points="0,340 700,318 700,400 0,400" fill="#8d8d8f"/>
  </svg>

  <p class="website">www.veltrixtech.com</p>
  <div class="brand">Veltrix Technologies</div>
</section>

</body>
</html>
```